Tomorrow-Ready Squared: The Definitive Guide to Improving Productivity, Refining Process and Bolsteri

Book Title: Tomorrow-Ready Squared
Subtitle: The Definitive Guide to Improving Productivity, Refining Process and Bolstering Profitability in Today's Disruptive Business Environment
Author's Name: Dana R. Marsh

The book is a marketing tool to support my consulting practice... www.vtrioadvisory.example I am uploading my brand standards. The cover needs to be eye catching and have an image of some sort.

Some Context
My Why
• Start in an unusual place------- total utter failure
o Landed my dream job - Build a Program Management Office from the ground up
 Emerging company growing for an IPO or acquisition
 Nothing but endless opportunity
 Promise of a life changing experience
o Things are seldom as the appear
 Leadership team was not aligned for cross-functional collaboration
 Breaking the silos was a larger challenge than one person could achieve
 Each silo was reinforcing their perceived sphere of influence and power
 Consultants were rolling through with wide varieties of advice. Nothing was truly being adopted
 I failed to implement the true value of the PMO and took an exit opportunity
o The Life Changing Promise was fulfilled… just not as anticipated
 Vtrio Advisory was born out of this experience and frustration
o The ah-ha moment lead to the basis of a new way of helping companies
 The visionary thought: Align People, Process and Technology
• Core foundation for all business sets stage for growth and the ability to be disruptive
• Business Process / Performance Measurement, Internal Controls, Organizational Change Management and Project Management
• Ten years of development created Adaptive Transformation = Future Proofing
o Adaptive Transformation is a series of agile processes that effectively influence corporate structure and culture, allowing the organization to evolve and thrive amidst disruptive market forces.
o Results = Process, Productivity and Profitability
• Common Challenges the things that keep us awake at night
o Inability to deliver strategic results
o Decision making takes too long and requires too many people
o It's the way we've always done it syndrome
o Providing products / solutions / service that do not speak to customers
o Everything takes too long… no real progress… same issues over and over again

Target Market(s)

C-Suite Executives looking to grow their companies

Font styles to use
Serif

Colors
a64599
0255a3
9ccb3b

Requirements
Must have
• Must use colors from the attached Brand Standards.
• Author Bio and Photo on back cover
Nice to have
• Conduit Medium Font
Should not have
• Cartoon type images

```html
<!DOCTYPE html>
<html lang="en">
<head>
<meta charset="utf-8">
<title>Tomorrow-Ready Squared – Book Cover</title>
<link rel="stylesheet" href="https://fonts.googleapis.com/css2?family=Cinzel:wght@400;600&family=Federo&family=Alegreya:ital@1&family=Signika:wght@400;500&display=swap">
<style>
  :root {
    --brand-blue: #0255a3;
    --brand-green: #9ccb3b;
    --brand-purple: #a64599;
    --page-bg: #f2f2f2;
    --white: #ffffff;
    --wood-dark: #4a2210;
    --wood-mid: #8a4a26;
    --wood-light: #b06a3a;
  }
  * { box-sizing: border-box; margin: 0; padding: 0; }
  html, body { width: 1200px; height: 800px; overflow: hidden; background: var(--page-bg); }
  .canvas { position: relative; width: 1200px; height: 800px; }

  .cover-spread {
    position: absolute; left: 60px; top: 13px;
    width: 1080px; height: 773px;
    background: var(--brand-blue);
    overflow: hidden;
  }
  .green-band {
    position: absolute; left: 0; bottom: 0; width: 100%; height: 101px;
    background: var(--brand-green);
  }

  /* Back cover */
  .back-title {
    position: absolute; left: 40px; top: 38px; width: 436px;
    text-align: center; font-family: 'Cinzel', serif; font-weight: 600;
    font-size: 26px; color: var(--brand-green); white-space: nowrap;
  }
  .back-title .accent { color: var(--white); }
  .back-subtitle {
    position: absolute; left: 40px; top: 78px; width: 436px;
    text-align: center; font-family: 'Alegreya', serif; font-style: italic;
    font-size: 13.5px; line-height: 16.5px; color: var(--white);
  }
  .back-rule {
    position: absolute; left: 85px; top: 151px; width: 375px; height: 3px;
    background: linear-gradient(90deg, rgba(156,203,59,0), var(--brand-green) 30%, var(--brand-green) 70%, rgba(156,203,59,0));
  }
  .author-bio {
    position: absolute; left: 58px; top: 180px; width: 401px;
    font-family: 'Signika', sans-serif; font-size: 9.4px; line-height: 14.4px;
    color: var(--white); text-align: justify;
  }
  .author-photo {
    float: left; width: 114px; height: 134px; margin: 0 8px 4px 0;
    background: radial-gradient(ellipse at 50% 40%, #bdbdbd 0%, #6b6b6b 45%, #1f1f1f 100%);
  }
  .author-bio .bio-name { color: var(--brand-green); font-weight: 500; }

  /* Spine */
  .spine {
    position: absolute; left: 505px; top: 40px; height: 560px; width: 56px;
    writing-mode: vertical-rl; display: flex; align-items: center; gap: 50px;
    font-family: 'Cinzel', serif; white-space: nowrap;
  }
  .spine-title { color: var(--brand-green); font-size: 26px; font-weight: 600; }
  .spine-title .accent { color: var(--white); }
  .spine-author { font-family: 'Federo', sans-serif; color: var(--white); font-size: 26px; }

  /* Front cover */
  .front-title {
    position: absolute; left: 570px; top: 38px; width: 506px;
    text-align: center; font-family: 'Cinzel', serif; font-weight: 600;
    line-height: 1;
  }
  .front-title span { display: block; }
  .front-title .line-1 { color: var(--brand-green); font-size: 66px; }
  .front-title .line-2 { color: var(--brand-green); font-size: 98px; margin-top: -4px; }
  .front-title .line-3 { color: var(--white); font-size: 80px; margin-top: -2px; }
  .front-subtitle {
    position: absolute; left: 570px; top: 275px; width: 506px;
    text-align: center; font-family: 'Alegreya', serif; font-style: italic;
    font-size: 18.5px; line-height: 22.5px; color: var(--white);
  }
  .cover-image {
    position: absolute; left: 564px; top: 383px; width: 516px; height: 288px;
    border-top: 8px solid #000; border-bottom: 2px solid #000;
    background:
      radial-gradient(ellipse at 50% 55%, var(--wood-light) 0%, var(--wood-mid) 45%, var(--wood-dark) 100%);
  }
  .front-author {
    position: absolute; left: 564px; top: 686px; width: 516px;
    text-align: center; font-family: 'Federo', sans-serif;
    font-size: 66px; line-height: 1; color: var(--brand-blue);
  }
</style>
</head>
<body>
<main class="canvas">
  <section class="cover-spread">
    <div class="green-band"></div>

    <article class="back-cover">
      <h2 class="back-title">Tomorrow-Ready <span class="accent">Squared</span></h2>
      <p class="back-subtitle">The Definitive Guide to Improving Productivity,<br>Refining Process and Bolstering Profitability in Today's<br>Disruptive Business Environment</p>
      <div class="back-rule"></div>
      <div class="author-bio">
        <div class="author-photo" role="img" aria-label="Black and white portrait photo of the author"></div>
        <p><span class="bio-name">DANA R. MARSH</span> is the Founder and CEO Of Vtrio Advisory. Vtrio Advisory elevates organizations in adapting and transforming quickly for achieving their strategic goals. Vtrio clients include Meridian Card Services, Crestline Health, Harborview Financial Network and The Red Mesa Utility Project and range from enterprise-level to medium sized organizations. A nationally recognized authority on organizational change management, Dana has contributed as a guest expert on numerous media outlets including Channel Nine, Metro One, Summit TV and Beacon News. Dana is a frequent speaker at conferences for business executives across the country. A resident of Desert Ridge, Arizona, Dana is an avid technology enthusiast and Valtari performance sports car driver who sits on the Halvorsen College of Business Information Systems Advisory Council and enjoys spending time with her family and hound dogs - Rusty and Biscuit.</p>
      </div>
    </article>

    <div class="spine">
      <span class="spine-title">Tomorrow-Ready <span class="accent">Squared</span></span>
      <span class="spine-author">Dana R. Marsh</span>
    </div>

    <article class="front-cover">
      <h1 class="front-title">
        <span class="line-1">Tomorrow-</span>
        <span class="line-2">Ready</span>
        <span class="line-3">Squared</span>
      </h1>
      <p class="front-subtitle">The Definitive Guide to Improving Productivity,<br>Refining Process and Bolstering Profitability in Today's<br>Disruptive Business Environment</p>
      <div class="cover-image" role="img" aria-label="Photo of a wooden shadow box with compartments holding a calculator, jars of cash, a small house, a shopping cart, tags and an office sign"></div>
      <p class="front-author">Dana R. Marsh</p>
    </article>
  </section>
</main>
</body>
</html>
```